Bright Current Swim Club

I am a Swim Club and want something that catches peoples eyes. Not too busy either. I have some photos of our logo and also pics of kids that are great quality if not I'm good with something you provide.

I want my email, phone number and website contact on it along with programs we offer. Highest Coaching Quality with High Performance Level 3, Age Group performance Level 2 and Fundamentals coaches Level 1. (Not sure how we can incorporate this)

Team Colours in Blue (Pool Blue)/ Black and White Grey is fine as well.
Spread it out over both sides!
Updates

Would like to keep to Team colours which are on my Logo Blue/Black / white you can add Grey as well. Would prefer the use of our logo or pictures with our Team Caps but do like pictures without team caps that are random swim pictures as well.

Target Market(s)

Parents/ kids/ athletes

Industry/Entity Type

Club

Font styles to use
Serif
Sans Serif

Colors
0592cd
ffffff

Requirements
Must have
• Programs we offer are Competitive Swim, Swim Academy, Fitness Swim, Adult Swim & Personal Training programs (Online). We coach from High performance athletes to developmental.

www.swimbcsc.example (Website)
coachdelia@swimbcsc.example (email)
555-614-2937 (Phone)

"We Teach Leadership"
"We are part of the Community"
"We Build Friendships that last a lifetime"
"We Teach Kids to Swim and LOVE the water"
Nice to have
• You can do your own background picture rather the ones I have sent

```html
<!DOCTYPE html>
<html lang="en">
<head>
<meta charset="utf-8">
<title>Bright Current Swim Club – Flyer</title>
<link href="https://fonts.googleapis.com/css2?family=Lato:wght@400;700;900&display=swap" rel="stylesheet">
<style>
  :root {
    --pool-blue: #0592cd;
    --pool-light: #3fb6e6;
    --water-a: #5cc6ee;
    --water-b: #1b8fc6;
    --ink: #231f20;
    --white: #ffffff;
    --backdrop: #e9ecef;
  }
  * { margin: 0; padding: 0; box-sizing: border-box; }
  html, body {
    width: 806px; height: 1200px; overflow: hidden;
    background: var(--backdrop);
    font-family: "Lato", Arial, sans-serif;
  }
  .canvas { position: relative; width: 806px; height: 1200px; }
  .flyer {
    position: absolute; background: var(--white); overflow: hidden;
    box-shadow: 0 2px 8px rgba(0,0,0,.18);
  }
  .flyer--front { left: 80px; top: 68px; width: 648px; height: 504px; }
  .flyer--back  { left: 80px; top: 622px; width: 646px; height: 500px; }
  .flyer__art { position: absolute; inset: 0; }
  .club-mark {
    position: absolute; display: flex; align-items: center; gap: 8px;
    font-weight: 700; font-size: 16px; letter-spacing: .5px;
    color: var(--ink); text-transform: uppercase; white-space: nowrap;
  }
  .club-mark__dot { width: 26px; height: 26px; border-radius: 50%; background: var(--pool-blue); flex: none; }
  .values { position: absolute; left: 16px; top: 234px; width: 318px; list-style: none; }
  .values__pill {
    height: 28px; border-radius: 14px; margin-bottom: 12px;
    color: var(--white); font-weight: 700; font-size: 14.5px;
    display: flex; align-items: center; justify-content: center;
  }
  .values__pill--dark { background: var(--ink); }
  .values__pill--blue { background: var(--pool-blue); }
  .programs-front {
    position: absolute; left: 20px; right: 20px; top: 453px;
    color: var(--white); font-weight: 700; font-size: 13.6px; line-height: 18px; text-align: center;
  }
  .programs-callout {
    position: absolute; left: 2px; top: 43px; width: 298px; height: 70px;
    background: var(--pool-blue); border-radius: 0 14px 14px 0;
    box-shadow: 0 4px 6px rgba(0,0,0,.15);
    color: var(--white); font-weight: 700; font-size: 10.2px; line-height: 13px;
    padding: 8px 10px 0 15px; white-space: nowrap;
  }
  .contact { position: absolute; left: 20px; width: 280px; text-align: center; color: var(--ink); }
  .contact__web, .contact__mail { font-weight: 700; font-size: 16.5px; line-height: 20px; }
  .contact__phone {
    display: flex; align-items: center; justify-content: center; gap: 6px;
    color: var(--pool-blue); font-weight: 700; font-size: 22px; line-height: 26px; margin-top: 2px;
  }
  .values-list {
    position: absolute; right: 18px; top: 380px; list-style: none; text-align: right;
    color: var(--white); font-weight: 700; font-size: 14.5px; line-height: 17px;
  }
</style>
</head>
<body>
<div class="canvas">

  <!-- Front side -->
  <section class="flyer flyer--front">
    <svg class="flyer__art" width="648" height="504" viewBox="0 0 648 504">
      <path d="M0,0 H300 C220,20 140,70 0,110 Z" fill="var(--pool-light)"/>
      <path d="M0,95 C120,60 220,20 300,0" stroke="var(--white)" stroke-width="6" fill="none"/>
      <path d="M648,230 C560,290 420,280 330,200 C420,300 560,300 648,260 Z" fill="var(--pool-blue)"/>
      <path d="M648,275 C560,320 470,300 400,255 C470,320 580,335 648,300 Z" fill="var(--ink)"/>
      <path d="M0,400 C160,385 320,425 460,430 C560,434 620,405 648,385 V504 H0 Z" fill="var(--ink)"/>
      <path d="M260,420 C400,445 540,440 648,350 V372 C560,440 420,448 260,420 Z" fill="var(--pool-blue)"/>
    </svg>
    <svg class="flyer__art" width="648" height="504" viewBox="0 0 648 504" role="img" aria-label="Photo of a young swimmer doing butterfly in a blue pool">
      <defs>
        <linearGradient id="waterFront" x1="0" y1="0" x2="1" y2="1">
          <stop offset="0" stop-color="#62c8ef"/>
          <stop offset="1" stop-color="#1d95cc"/>
        </linearGradient>
      </defs>
      <path d="M300,0 H648 V205 C560,250 430,250 360,185 C320,140 290,90 300,0 Z" fill="url(#waterFront)"/>
      <path d="M300,0 C290,90 320,140 360,185 C430,250 560,250 648,205" stroke="var(--white)" stroke-width="5" fill="none"/>
    </svg>
    <div class="club-mark" style="left:40px; top:186px;"><span class="club-mark__dot"></span>Bright Current Swim Club</div>
    <ul class="values">
      <li class="values__pill values__pill--dark">We Teach Leadership</li>
      <li class="values__pill values__pill--blue">We are part of the Community</li>
      <li class="values__pill values__pill--dark">We Build Friendship that lasts for a lifetime</li>
      <li class="values__pill values__pill--blue">We Teach Kids to Swim and LOVE the water</li>
    </ul>
    <p class="programs-front">We offer Competitive Swimming, Swim Academy, Fitness Swim, Adult Swim &amp; Personal<br>Training programs (Online). We coach from High performance athletes to developmental.</p>
  </section>

  <!-- Back side -->
  <section class="flyer flyer--back">
    <svg class="flyer__art" width="646" height="500" viewBox="0 0 646 500">
      <path d="M350,0 H380 C330,70 340,160 420,205 C480,235 570,235 646,210 V232 C560,255 460,250 400,210 C330,160 320,70 350,0 Z" fill="var(--pool-blue)"/>
      <path d="M380,205 C470,250 570,245 646,225 V240 C560,262 460,258 380,205 Z" fill="var(--ink)"/>
      <path d="M0,362 C140,358 280,342 400,308 C300,350 150,385 0,400 Z" fill="var(--ink)"/>
      <path d="M0,408 C160,400 300,345 460,304 C540,286 610,284 646,287 V500 H0 Z" fill="var(--pool-blue)"/>
      <path d="M0,405 C150,396 300,342 460,301" stroke="var(--white)" stroke-width="6" fill="none"/>
    </svg>
    <svg class="flyer__art" width="646" height="500" viewBox="0 0 646 500" role="img" aria-label="Photo of three smiling young club swimmers in team jackets at an indoor pool">
      <defs>
        <linearGradient id="poolBack" x1="0" y1="0" x2="1" y2="1">
          <stop offset="0" stop-color="#b9d6e6"/>
          <stop offset=".5" stop-color="#3e6fa8"/>
          <stop offset="1" stop-color="#1c2f6e"/>
        </linearGradient>
      </defs>
      <path d="M372,0 H646 V200 C570,222 480,218 420,185 C360,140 350,60 372,0 Z" fill="url(#poolBack)"/>
    </svg>
    <p class="programs-callout">We offer Competitive Swimming,Swim Academy,<br>Fitness Swim, Adult Swim &amp; Personal Training programs<br>(Online).We coach from High performance athletes<br>to developmental.</p>
    <div class="club-mark" style="left:44px; top:238px;"><span class="club-mark__dot"></span>Bright Current Swim Club</div>
    <div class="contact" style="top:270px;">
      <p class="contact__web">www.swimbcsc.example</p>
      <p class="contact__mail">coachdelia@swimbcsc.example</p>
      <p class="contact__phone">
        <svg width="20" height="20" viewBox="0 0 20 20" aria-hidden="true">
          <rect width="20" height="20" rx="4" fill="var(--pool-blue)"/>
          <path d="M6,4 L8,4 L9,7 L7.5,8.2 C8.3,10 9.8,11.6 11.8,12.5 L13,11 L16,12 L16,14 C16,15 15,16 14,16 C8.5,15.5 4.5,11.5 4,6 C4,5 5,4 6,4 Z" fill="var(--white)"/>
        </svg>555-614-2937</p>
    </div>
    <ul class="values-list">
      <li>We Teach Leadership</li>
      <li>We are part of the Community</li>
      <li>We Build Friendship that lasts for a lifetime</li>
      <li>We Teach Kids to Swim and LOVE the water</li>
    </ul>
  </section>

</div>
</body>
</html>
```